Adventure Business Cards

Please check out our website for style
Vertical card
Details:
Side 1
Logo
Business name: Kestrel Point Wildland Tours
Name: Colin Warbeck
Role: Director
Email: info@kestrelpointtours.com
Address: PO Box 71, Marlin Cove NSW 2471
Phone: +61 2 5550 1847
Web address: www.kestrelpointtours.com
Side 2
Taking pictures?
A Friendwall and Pixlane logo
Tag us in your pictures with
#kpwildtours
@kpwildtours
www.kestrelpointtours.com
Details:
Side 1
Logo
Name: Colin Warbeck
Role: Director
Phone: +61 2 5550 1847
Side 2
Taking pictures?
#kpwildtours
@kpwildtours

```html
<!DOCTYPE html>
<html lang="en">
<head>
<meta charset="utf-8">
<title>Kestrel Point Wildland Tours – Business Card</title>
<link rel="stylesheet" href="https://fonts.googleapis.com/css2?family=Comfortaa:wght@400;700&display=swap">
<style>
  :root {
    --page: #ebe7e0;
    --card: #f4f4f4;
    --card-edge: #dcdcdc;
    --ink: #1c1c1c;
    --ink-soft: #3a3a3a;
    --accent: #f2c415;
    --band: #1a1a1a;
    --social: #2f8fd0;
    --forest-light: #c9d4c0;
    --forest-mid: #6f8f4f;
    --forest-dark: #2f4a25;
  }
  * { box-sizing: border-box; margin: 0; padding: 0; }
  html, body { width: 1200px; height: 780px; overflow: hidden; }
  body {
    background: var(--page);
    font-family: "Comfortaa", sans-serif;
    color: var(--ink);
    position: relative;
  }
  .card {
    position: absolute;
    top: 90px;
    width: 340px;
    height: 600px;
    background: linear-gradient(160deg, #ffffff 0%, var(--card) 60%, var(--card-edge) 100%);
    box-shadow: 0 10px 28px rgba(0,0,0,.18);
    overflow: hidden;
  }
  .card--front { left: 190px; }
  .card--back { left: 670px; }

  /* brand mark */
  .brand {
    display: flex;
    align-items: center;
    justify-content: center;
    gap: 12px;
  }
  .brand__dot {
    width: 34px; height: 34px; border-radius: 50%;
    background: var(--accent);
    flex: none;
  }
  .brand__name {
    font-weight: 700;
    font-size: 17px;
    line-height: 1.3;
    color: var(--ink);
    text-transform: uppercase;
    letter-spacing: .04em;
    text-align: left;
  }

  /* front */
  .card--front .brand { margin-top: 74px; padding: 0 30px; }
  .person { text-align: center; margin-top: 50px; }
  .person__name { font-weight: 700; font-size: 27px; color: var(--accent); }
  .person__role { font-weight: 700; font-size: 15px; margin-top: 4px; }
  .address {
    text-align: center; font-size: 16px; line-height: 1.4;
    margin: 22px auto 0; width: 280px; color: var(--ink-soft);
  }
  .divider { width: 270px; height: 1px; background: #555; margin: 16px auto 12px; }
  .contact { text-align: center; font-size: 15px; color: var(--ink-soft); }
  .contact__icon { display: block; margin: 0 auto 4px; }
  .contact + .contact { margin-top: 12px; }
  .front-band {
    position: absolute; left: 0; right: 0; bottom: 0; height: 82px;
    background: var(--band);
    border-top: 3px solid var(--accent);
    display: flex; align-items: center; justify-content: center;
    color: #e8e8e8; font-size: 16px; letter-spacing: .02em;
  }

  /* back */
  .socials { position: absolute; top: 22px; right: 26px; text-align: right; }
  .social { display: flex; align-items: center; justify-content: flex-end; gap: 8px; font-size: 14px; line-height: 18px; color: var(--ink-soft); }
  .social + .social { margin-top: 6px; }
  .social__square { width: 18px; height: 18px; background: var(--social); flex: none; }
  .social__label { font-size: 10px; color: var(--social); font-weight: 700; }
  .card--back .brand { position: absolute; top: 140px; left: 24px; right: 24px; justify-content: flex-start; }
  .forest {
    position: absolute; left: 0; right: 0; top: 232px; height: 250px;
    border-top: 4px solid var(--band);
    border-bottom: 4px solid var(--band);
    background: linear-gradient(150deg, var(--forest-light) 0%, var(--forest-mid) 45%, var(--forest-dark) 100%);
  }
  .back-web {
    position: absolute; left: 0; right: 0; bottom: 44px;
    text-align: center; font-size: 15px; color: var(--ink-soft);
  }
</style>
</head>
<body>

<section class="card card--front">
  <div class="brand">
    <span class="brand__dot"></span>
    <span class="brand__name">Kestrel Point<br>Wildland Tours</span>
  </div>

  <div class="person">
    <p class="person__name">Colin Warbeck</p>
    <p class="person__role">Director</p>
  </div>

  <p class="address">PO Box 71, Marlin Cove<br>NSW 2471</p>
  <div class="divider"></div>

  <p class="contact">
    <svg class="contact__icon" width="22" height="18" viewBox="0 0 22 18" aria-hidden="true">
      <rect width="22" height="18" rx="2" fill="#f2c415"/>
      <path d="M7 4c1 0 2 2.5 1.5 3.2L7.6 8c.6 1.4 1.6 2.4 3 3l.8-.9c.7-.5 3.2.5 3.2 1.5 0 1-1.2 2.2-2.4 2.2C8.8 13.8 5 10 5 6.4 5 5.2 6 4 7 4z" fill="#fff"/>
    </svg>
    +61 2 5550 1847
  </p>
  <p class="contact">
    <svg class="contact__icon" width="22" height="16" viewBox="0 0 22 16" aria-hidden="true">
      <rect width="22" height="16" rx="1" fill="#f2c415"/>
      <path d="M2 2l9 7 9-7" fill="none" stroke="#fff" stroke-width="1.6"/>
    </svg>
    info@kestrelpointtours.com
  </p>

  <div class="front-band">www.kestrelpointtours.com</div>
</section>

<section class="card card--back">
  <div class="socials">
    <p class="social"><span class="social__label">Friendwall</span><span class="social__square"></span></p>
    <p class="social">#kpwildtours</p>
    <p class="social"><span class="social__label">Pixlane</span><span class="social__square"></span></p>
    <p class="social">@kpwildtours</p>
  </div>

  <div class="brand">
    <span class="brand__dot"></span>
    <span class="brand__name">Kestrel Point<br>Wildland Tours</span>
  </div>

  <div class="forest" role="img" aria-label="Photograph of a misty rainforest with mossy trunks and ferns"></div>

  <p class="back-web">www.kestrelpointtours.com</p>
</section>

</body>
</html>
```